**** Web design project for VornaSoft ****

For my ICT company VornaSoft I need a website.

We design, build and host web-applications and we have our own CMS product. In the references part we want to show sample websites (thumbnails) + links.

It should look modern (WEB 2.0), rounded corners.

I want the following menu' s:
- Home
- Services
- References
- News
- About VornaSoft
- Contact

Sample websites:
See attachments
http://www.plumvest.com
http://www.gadomirbureauwerk.nl

Reason: Want to take some time for feedback and improvements.

Reason: I'm waiting for a black background, with shadow and ambient light. You'll make a good chance!

Industry/Entity Type

It Company

Requirements
Must have
• - Fixed width (1024px), should fit on an IPad2
- Language selection English/Dutch
- Chirpline/Friendwall/LinkedIn/RSS icons
- Footer for Terms of use and Copyrights
- Search box
- 3 (or more) boxes for information i.e. news, blog or advertisements
Nice to have
• - Footer Site Map
- Contrasting background outside borders
- wide image (rotator) (with transperant sentence block)
- Shadow

```html
<!DOCTYPE html>
<html lang="en">
<head>
<meta charset="utf-8">
<title>VornaSoft – Web Applications</title>
<link href="https://fonts.googleapis.com/css2?family=Titillium+Web:wght@300;400;600&display=swap" rel="stylesheet">
<style>
:root{
  --page-bg:#eef2f6;
  --panel:#f8f8f8;
  --panel-line:#d9d9d9;
  --text:#555a5f;
  --heading:#3d4247;
  --blue:#1aa3e6;
  --blue-dark:#0d86c7;
  --link:#1a9fe0;
  --footer:#dcdcdc;
  --footer-text:#707070;
  --bar:#4b4b4b;
}
*{box-sizing:border-box;margin:0;padding:0}
html,body{width:994px;height:1200px;overflow:hidden}
body{background:linear-gradient(#f7f9fb,var(--page-bg) 100px,var(--page-bg));font-family:"Titillium Web",sans-serif;color:var(--text);position:relative}
.abs{position:absolute}
.site-header{position:absolute;left:0;top:0;width:994px;height:94px;background:linear-gradient(#f9fbfd,#eef3f8);border-bottom:1px solid #d8dde2}
.brand{left:79px;top:18px;display:flex;align-items:center;gap:10px}
.brand-dot{width:52px;height:52px;border-radius:50%;background:var(--blue-dark)}
.brand-name{font-size:28px;font-weight:400;color:#4d6a7a;letter-spacing:.5px}
.search{left:780px;top:10px;width:81px;height:15px;border:1px solid #cfd3d7;background:#fff;font-size:8px;color:#999;padding:1px 4px;line-height:12px}
.lang{top:11px;height:11px;width:17px;font-size:7px;font-weight:600;color:#fff;text-align:center;line-height:11px}
.lang.en{left:879px;background:#3a4f9c}
.lang.nl{left:901px;background:#c4323c}
.main-nav{left:543px;top:35px;display:flex;gap:0;font-size:13px;color:var(--heading)}
.main-nav a{text-decoration:none;color:inherit;padding:0 8.5px;line-height:25px;height:25px}
.main-nav a.active{background:linear-gradient(#35b8f0,#1196dc);color:#fff;border-radius:7px;padding:0 8px}
.panel{left:78px;top:94px;width:838px;height:1096px;background:var(--panel);box-shadow:0 0 3px rgba(0,0,0,.25)}
.rule{height:1px;background:var(--panel-line)}
h1,h2,h3{font-weight:400;color:var(--heading)}
.hero-title{left:95px;top:113px;font-size:18px}
.hero-text{left:95px;top:145px;width:465px;font-size:12.5px;line-height:17.2px;font-weight:300}
.btn-learn{left:95px;top:281px;width:180px;height:58px;border-radius:3px;background:linear-gradient(#3bc0f3,#0f94d8);border:1px solid #0d7fbb;font-size:21px;font-weight:600;color:#2a3e4d;text-align:center;line-height:56px}
.hero-art{left:581px;top:105px;width:324px;height:248px;background:linear-gradient(135deg,#2a75cf,#1257b5);border-radius:2px}
.reasons-title{left:95px;top:390px;font-size:16px}
.reason h3{font-size:16px;position:absolute;top:0;left:37px;white-space:nowrap}
.reason p{position:absolute;left:37px;top:35px;width:210px;font-size:10.5px;line-height:17.2px;font-weight:300}
.reason svg{position:absolute;left:0;top:0}
.btn-services{left:454px;top:562px;width:87px;height:25px;border:1px solid #c9c9c9;border-radius:3px;background:linear-gradient(#fff,#ececec);font-size:10.5px;text-align:center;line-height:23px;color:#666}
.sec-title{font-size:16px}
.clients-text{left:95px;top:621px;width:540px;font-size:10.5px;line-height:17.2px;font-weight:300}
.client-strip{left:95px;top:678px;width:535px;height:35px;background:#fff;display:flex;align-items:center;justify-content:space-around;font-size:13px;font-weight:600;color:#8a8a8a}
.ref{top:791px;width:165px}
.ref-thumb{width:162px;height:106px;background:linear-gradient(#5ab4e6,#2f8fcd 60%,#d8e7f2);border:2px solid #fff;box-shadow:0 1px 3px rgba(0,0,0,.35)}
.ref-plus{position:absolute;right:-6px;top:-6px;width:24px;height:24px;border-radius:50%;background:#eee;border:1px solid #ccc;text-align:center;line-height:21px;font-size:18px;font-weight:600;color:#666}
.ref h3{font-size:12.5px;margin-top:12px;font-weight:600}
.ref p{font-size:10.5px;line-height:17.2px;font-weight:300}
.news-item{left:654px;width:216px;height:63px;background:#efefef;border:1px solid #dcdcdc}
.news-thumb{position:absolute;left:8px;top:7px;width:49px;height:49px;background:linear-gradient(135deg,#555,#1a1a1a);border:2px solid #fff;box-shadow:0 0 2px rgba(0,0,0,.4)}
.news-body{position:absolute;left:66px;top:5px;font-size:8px;line-height:10px;color:#444}
.news-body strong{font-weight:600;display:block;margin-bottom:2px}
.news-body .meta{margin-top:8px}
.news-body .meta a{color:var(--link);text-decoration:none}
.site-footer{left:78px;top:1054px;width:838px;height:103px;background:var(--footer)}
.foot-col{top:1068px;font-size:7.5px;line-height:10.3px;color:var(--footer-text)}
.foot-col h4{font-size:7.5px;font-weight:600;color:#444;border-bottom:1px solid #aaa;padding-bottom:2px;margin-bottom:5px;width:100px}
.foot-brand{left:733px;top:1078px;display:flex;align-items:center;gap:8px}
.foot-brand .brand-dot{width:48px;height:48px;background:#8a8a8a}
.foot-brand .brand-name{color:#777;font-size:24px}
.copy-bar{left:78px;top:1157px;width:838px;height:33px;background:var(--bar);color:#e8e8e8;font-size:10.5px;line-height:33px;padding-left:17px}
.social{position:absolute;right:17px;top:0;display:flex;gap:9px;align-items:center}
.social span{font-size:8px;display:flex;align-items:center;gap:3px;color:#eee}
.social i{width:12px;height:12px;border-radius:2px;display:inline-block}
</style>
</head>
<body>
<header class="site-header">
  <div class="abs brand"><span class="brand-dot"></span><span class="brand-name">VornaSoft</span></div>
  <div class="abs search">Search...</div>
  <div class="abs lang en">EN</div>
  <div class="abs lang nl">NL</div>
  <nav class="abs main-nav">
    <a class="active" href="#">Home</a><a href="#">Services</a><a href="#">References</a><a href="#">News</a><a href="#">About VornaSoft</a><a href="#">Contact</a>
  </nav>
</header>

<main>
  <div class="abs panel"></div>

  <h1 class="abs hero-title">We Creat Great &amp; Easy-to-Use Applications !</h1>
  <p class="abs hero-text">Lorem ipsum dolor sit amet, consectetur adipisicing elit, sed do eiusmod tempor incidid-unt ut labore et dolore magna aliqua. Ut enim ad minim veniam, quis nostrud exercitation ullamco laboris nisi ut aliquip ex ea commodo consequat.Lorem ipsum dolor sit amet, consectetur adipisicing elit, sed do eiusmod tempor incididunt ut labore et dolore magna aliqua. Ut enim ad minim veniam, quis nostrud exercitation ullamco laboris nisi ut aliquip ex ea commodo consequat.</p>
  <div class="abs btn-learn">Learn More</div>
  <div class="abs hero-art" role="img" aria-label="Stack of blue technical blueprint sheets"></div>

  <div class="abs rule" style="left:78px;top:375px;width:838px"></div>

  <h2 class="abs reasons-title">Reasons why you love to use VornaSoft</h2>
  <div class="abs reason" style="left:95px;top:427px">
    <svg width="24" height="28" viewBox="0 0 24 28"><rect x="1" y="3" width="22" height="24" rx="2" fill="#f3e3c6" stroke="#c0783a" stroke-width="2"/><rect x="7" y="1" width="10" height="5" fill="#888"/><path d="M5 11h3M5 16h3M5 21h3M11 11h8M11 16h8M11 21h8" stroke="#555" stroke-width="1.5"/></svg>
    <h3>Problem Solver</h3>
    <p>Lorem ipsum dolor sit amet, consectetur adipisicing elit, sed do eiusmod tempor incidid-unt ut labore et dolore magna aliqua. Ut enim ad minim veniam, quis nostrud exercitation ullamco laboris nisi ut aliquip ex ea commodo.</p>
  </div>
  <div class="abs reason" style="left:366px;top:423px;width:260px">
    <svg width="28" height="22" viewBox="0 0 28 22"><rect x="1" y="1" width="26" height="20" fill="#1c2630" stroke="#888"/><path d="M4 5l3 2-3 2" stroke="#3bb" fill="none"/></svg>
    <h3 style="left:40px">Innovation and reliability</h3>
    <p style="left:41px;top:37px">Lorem ipsum dolor sit amet, consectetur adipisicing elit, sed do eiusmod tempor incidid-unt ut labore et dolore magna aliqua. Ut enim ad minim veniam, quis nostrud exercitation ullamco laboris nisi ut aliquip ex ea commodo.</p>
  </div>
  <div class="abs reason" style="left:653px;top:423px;width:260px">
    <svg width="30" height="24" viewBox="0 0 30 24"><ellipse cx="15" cy="10" rx="13" ry="8" fill="#fff" stroke="#bbb"/><path d="M8 16l-2 6 7-5" fill="#fff" stroke="#bbb"/></svg>
    <h3 style="left:41px">Popular community</h3>
    <p style="left:41px;top:37px">Lorem ipsum dolor sit amet, consectetur adipisicing elit, sed do eiusmod tempor incidid-unt ut labore et dolore magna aliqua. Ut enim ad minim veniam, quis nostrud exercitation ullamco laboris nisi ut aliquip ex ea commodo.</p>
  </div>

  <div class="abs rule" style="left:78px;top:572px;width:838px"></div>
  <div class="abs btn-services">Our Services</div>

  <h2 class="abs sec-title" style="left:95px;top:590px">Clients Who Used VornaSoft</h2>
  <p class="abs clients-text">Lorem ipsum dolor sit amet, consectetur adipisicing elit, sed do eiusmod tempor incididunt ut labore et dolore magna aliqua. Ut enim ad minim veniam, quis nostrud exercitation ullamco laboris nisi ut aliquip ex ea commodo consequat.Lorem ipsum dolor sit amet, consectetur adipisicing elit, sed do eiusmod tempor incididunt ut labore et dolore</p>
  <div class="abs client-strip"><span>Yarrow Finance</span><span>TechBramble</span><span>Mixwell</span><span>The Brightline Web</span></div>

  <div class="abs rule" style="left:95px;top:739px;width:535px"></div>
  <h2 class="abs sec-title" style="left:95px;top:750px">Look Our References</h2>

  <article class="abs ref" style="left:97px"><div style="position:relative"><div class="ref-thumb" role="img" aria-label="Sample website screenshot"></div><span class="ref-plus">+</span></div><h3>Reference Title</h3><p>Lorem ipsum dolor sit amet, consecte-tur adipisicing elit, sed do eiusmod tempor incididunt ut labore et dolore magna aliqua. Ut enim ad minim</p></article>
  <article class="abs ref" style="left:281px"><div style="position:relative"><div class="ref-thumb" role="img" aria-label="Sample website screenshot"></div><span class="ref-plus">+</span></div><h3>Reference Title</h3><p>Lorem ipsum dolor sit amet, consecte-tur adipisicing elit, sed do eiusmod tempor incididunt ut labore et dolore magna aliqua. Ut enim ad minim</p></article>
  <article class="abs ref" style="left:465px"><div style="position:relative"><div class="ref-thumb" role="img" aria-label="Sample website screenshot"></div><span class="ref-plus">+</span></div><h3>Reference Title</h3><p>Lorem ipsum dolor sit amet, consecte-tur adipisicing elit, sed do eiusmod tempor incididunt ut labore et dolore magna aliqua. Ut enim ad minim</p></article>

  <h2 class="abs sec-title" style="left:654px;top:590px">Recent News</h2>
  <div class="abs news-item" style="top:627px"><div class="news-thumb" role="img" aria-label="News photo"></div><div class="news-body"><strong>News Title Here</strong>Lorem ipsum dolor sit amet,<br>consectetur adipisicing elit, sed do<div class="meta">Posted on 20 Dec 2012 | <a href="#">Read More</a></div></div></div>
  <div class="abs news-item" style="top:696px"><div class="news-thumb" role="img" aria-label="News photo"></div><div class="news-body"><strong>News Title Here</strong>Lorem ipsum dolor sit amet,<br>consectetur adipisicing elit, sed do<div class="meta">Posted on 20 Dec 2012 | <a href="#">Read More</a></div></div></div>
  <div class="abs news-item" style="top:764px"><div class="news-thumb" role="img" aria-label="News photo"></div><div class="news-body"><strong>News Title Here</strong>Lorem ipsum dolor sit amet,<br>consectetur adipisicing elit, sed do<div class="meta">Posted on 20 Dec 2012 | <a href="#">Read More</a></div></div></div>
  <div class="abs news-item" style="top:833px"><div class="news-thumb" role="img" aria-label="News photo"></div><div class="news-body"><strong>News Title Here</strong>Lorem ipsum dolor sit amet,<br>consectetur adipisicing elit, sed do<div class="meta">Posted on 20 Dec 2012 | <a href="#">Read More</a></div></div></div>
  <div class="abs news-item" style="top:901px"><div class="news-thumb" role="img" aria-label="News photo"></div><div class="news-body"><strong>News Title Here</strong>Lorem ipsum dolor sit amet,<br>consectetur adipisicing elit, sed do<div class="meta">Posted on 20 Dec 2012 | <a href="#">Read More</a></div></div></div>
  <div class="abs news-item" style="top:970px"><div class="news-thumb" role="img" aria-label="News photo"></div><div class="news-body"><strong>News Title Here</strong>Lorem ipsum dolor sit amet,<br>consectetur adipisicing elit, sed do<div class="meta">Posted on 20 Dec 2012 | <a href="#">Read More</a></div></div></div>
</main>

<footer>
  <div class="abs site-footer"></div>
  <div class="abs foot-col" style="left:95px"><h4>ABOUT US</h4>About Us<br>The VornaSoft Difference<br>Customers &amp; Testimonials<br>Awards<br>Events</div>
  <div class="abs foot-col" style="left:213px"><h4>REFERENCES</h4>Reference 1<br>Another Reference<br>Unique Reference here</div>
  <div class="abs foot-col" style="left:332px"><h4 style="width:195px">SERVICES</h4><div style="display:flex;gap:25px"><div>Application<br>Designing<br>User Interface<br>UX<br>Services widget</div><div>Application<br>Designing<br>User Interface<br>UX</div></div></div>
  <div class="abs foot-col" style="left:527px"><h4>NEWS</h4>News Title Here<br>News Title Here<br>News Title Here<br>News Title Here<br>News Title Here</div>
  <div class="abs foot-brand"><span class="brand-dot"></span><span class="brand-name">VornaSoft</span></div>
  <div class="abs copy-bar">Copyright © 2012 VornaSoft. All rights reserved.
    <div class="social">
      <span><i style="background:#f08a24"></i>Feed</span>
      <span><i style="background:#4fb8e4"></i>Chirpline</span>
      <span><i style="background:#3b5a9a"></i>Friendwall</span>
      <span><i style="background:#c4302b"></i>ClipHub</span>
      <span><i style="background:#1ab7ea"></i>Reelnook</span>
    </div>
  </div>
</footer>
</body>
</html>
```